Cedar Basin CBD Apothecary needs label for CBD capsule bottles

I need a 1 1/2"H x 3.5" W label for a cobalt blue glass pill bottle. Looking for apothecary look, but not over the top. I would like a yellow background (ccff00), or combination thereof, and my company logo/name, in addition to the text "PURE CBD CRYSTAL ISOLATE", Dietary Supplement, Ingredients: 99.1% Cannabidiol Crystal Isolate, Lab Tested, ZERO THC, NO FILLERS, Keep Out of Reach of Children, Serving Suggestion: Take one PlantaShell Daily, increase dosage as needed, Storage- cool dry place away from light and heat, www.cbcbdshop.com

Target Market(s)

Adults with health issues, all ages.

Industry/Entity Type

Health And Wellness

Font styles to use
Other font styles liked:
• similar to Algerian. Apothecary fonts.

Colors
fbee3d

Requirements
Must have
• Logo and Company name, "CEDAR BASIN CBD APOTHECARY"
• Yellow to contrast cobalt blue bottles
Nice to have
• Made in Joshua Tree, CA.
• Vegan Capsules
• NO GMO
Should not have
• no pot leaves or anything overtly cannabis related. No script fonts.

```html
<!DOCTYPE html>
<html lang="en">
<head>
<meta charset="utf-8">
<title>Cedar Basin CBD Apothecary – Pure CBD Crystal Isolate Label</title>
<link href="https://fonts.googleapis.com/css2?family=Cinzel:wght@600;700&family=EB+Garamond:wght@500&display=swap" rel="stylesheet">
<style>
  :root {
    --page: #eef0e4;
    --white: #ffffff;
    --leaf: #8cc63f;
    --leaf-soft: #d6ecb8;
    --chartreuse: #c9d82a;
    --plum: #6e2158;
    --plum-dark: #5a1848;
    --gold: #dfe63a;
    --badge: #6b8f2a;
  }
  html, body {
    margin: 0;
    width: 1200px;
    height: 1200px;
    overflow: hidden;
    background: var(--page);
  }
  .label {
    position: absolute;
    left: 220px;
    top: 120px;
    width: 760px;
    height: 960px;
    overflow: hidden;
    background: var(--white);
    box-shadow: 0 6px 24px rgba(0,0,0,0.12);
  }
  .label-art {
    position: absolute;
    inset: 0;
  }
  .brand {
    position: absolute;
    top: 60px;
    left: 0;
    width: 760px;
    display: flex;
    flex-direction: column;
    align-items: center;
    gap: 14px;
  }
  .brand-mark {
    width: 22px;
    height: 22px;
    border-radius: 50%;
    background: var(--plum);
  }
  .brand-name {
    text-align: center;
    font-family: "Cinzel", serif;
    font-weight: 600;
    font-size: 26px;
    letter-spacing: 2px;
    line-height: 1.3;
    color: var(--plum);
  }
  .product-title {
    position: absolute;
    top: 238px;
    left: 0;
    width: 776px;
    text-align: center;
    font-family: "Cinzel", serif;
    font-weight: 700;
    font-size: 112px;
    line-height: 100px;
    color: var(--plum);
    margin: 0;
  }
  .product-title span { display: block; }
  .product-type {
    position: absolute;
    top: 634px;
    left: 183px;
    width: 400px;
    text-align: center;
    font-family: "Cinzel", serif;
    font-weight: 700;
    font-size: 44px;
    line-height: 58px;
    letter-spacing: 1px;
    color: var(--gold);
  }
  .origin {
    position: absolute;
    top: 764px;
    left: 222px;
    width: 312px;
    height: 40px;
    background: var(--gold);
    text-align: center;
    font-family: "EB Garamond", serif;
    font-weight: 500;
    font-size: 22px;
    line-height: 40px;
    color: var(--plum-dark);
  }
  .badge-vegan {
    position: absolute;
    left: 592px;
    top: 706px;
    width: 150px;
    height: 58px;
    border-radius: 29px;
    background: var(--badge);
    opacity: 0.85;
  }
  .badge-nongmo {
    position: absolute;
    left: 594px;
    top: 786px;
    width: 130px;
    height: 130px;
    border-radius: 50%;
    background: var(--badge);
    opacity: 0.85;
  }
</style>
</head>
<body>
  <main class="label">
    <svg class="label-art" width="760" height="960" viewBox="0 0 760 960" aria-hidden="true">
      <defs>
        <linearGradient id="top-wash" x1="0" y1="0" x2="0" y2="1">
          <stop offset="0" stop-color="#8cc63f"/>
          <stop offset="0.45" stop-color="#d6ecb8"/>
          <stop offset="1" stop-color="#ffffff" stop-opacity="0"/>
        </linearGradient>
      </defs>
      <rect width="760" height="230" fill="url(#top-wash)"/>
      <path d="M0,548 C250,570 560,440 760,250 L760,960 L0,960 Z" fill="#c9d82a"/>
      <path d="M0,820 C210,670 500,460 760,268 L760,960 L0,960 Z" fill="#6e2158"/>
    </svg>

    <div class="brand">
      <span class="brand-mark"></span>
      <div class="brand-name">Cedar Basin<br>CBD Apothecary</div>
    </div>

    <h1 class="product-title"><span>PURE</span><span>CBD</span></h1>

    <div class="product-type">CRYSTAL<br>ISOLATE</div>

    <div class="origin">Made in Joshua Tree, CA.</div>

    <div class="badge-vegan" role="img" aria-label="Vegan badge"></div>
    <div class="badge-nongmo" role="img" aria-label="Made with non-GMO ingredients badge"></div>
  </main>
</body>
</html>
```